Beautiful collection of labels for unique hgh end food proucts

We are a online retailer of high end food and are looking for a design of 5 labels for our collection of products. Our products are quality, high end products Made in Italy by artisans. We want to create labels that are simple, elegant, modern and visually powerful. The labels will go on our boxes that are shiny chrome and strictly similar for most of our products. The labels are what differentiate one box from another and one product from another.

Reason: Merry Xmas to All

Target Market(s)

Consumers of High Quality Food Products

Industry/Entity Type

Online

Requirements
Must have
• Strong clear minimalist theme driven by patterns repeated throughot the series of labels

```html
<!DOCTYPE html>
<html lang="en">
<head>
<meta charset="UTF-8">
<title>For My Friends – Label Series</title>
<link href="https://fonts.googleapis.com/css2?family=Lobster&family=Great+Vibes&family=Monsieur+La+Doulaise&family=Mrs+Saint+Delafield&family=Exo+2:wght@500&family=Montserrat:wght@600;700&display=swap" rel="stylesheet">
<style>
  :root {
    --ink: #000000;
    --paper: #ffffff;
    --rule: #6b6b6b;
  }
  * { margin: 0; padding: 0; box-sizing: border-box; }
  html, body { width: 1200px; height: 1000px; overflow: hidden; background: var(--ink); }
  .sheet { position: relative; width: 1200px; height: 1000px; background: var(--ink); }

  .label {
    position: absolute;
    width: 409px;
    height: 299px;
    background: var(--paper);
    border: 1px solid #cfcfcf;
  }
  .col-left { left: 139px; }
  .col-right { left: 667px; }
  .row-1 { top: 20px; }
  .row-2 { top: 344px; }
  .row-3 { top: 673px; }

  .brand {
    position: absolute;
    left: 0; right: 0;
    top: 184px;
    text-align: center;
    color: var(--ink);
  }
  .brand-name {
    display: block;
    font-family: "Montserrat", sans-serif;
    font-weight: 700;
    font-size: 50px;
    line-height: 60px;
    letter-spacing: 1px;
  }
  .brand-product {
    display: block;
    margin-top: 4px;
    font-family: "Montserrat", sans-serif;
    font-weight: 700;
    font-size: 13px;
    letter-spacing: 0.62em;
    padding-left: 0.62em;
  }

  /* Variant 1: hanging tab */
  .tag-tab {
    position: absolute;
    left: 110px; top: 0;
    width: 175px; height: 115px;
    background: var(--ink);
    border-radius: 0 0 14px 14px;
    color: var(--paper);
    font-family: "Lobster", cursive;
    font-size: 35px;
    line-height: 46px;
    text-align: center;
    padding-top: 12px;
  }

  /* Variant 2: flowing lowercase script */
  .tag-flow {
    position: absolute;
    left: 0; right: 0; top: 12px;
    text-align: center;
    font-family: "Great Vibes", cursive;
    font-size: 76px;
    line-height: 110px;
    color: var(--ink);
  }

  /* Variant 3: outlined plate */
  .tag-plate {
    position: absolute;
    left: 58px; top: 61px;
    width: 288px; height: 61px;
    border: 1.5px solid var(--ink);
    border-radius: 0 0 14px 0;
    font-family: "Lobster", cursive;
    font-size: 31px;
    line-height: 58px;
    text-align: center;
    color: var(--ink);
  }

  /* Variant 4: underlined formal script */
  .tag-ruled {
    position: absolute;
    left: 17px; top: 40px;
    width: 370px;
    text-align: center;
    font-family: "Monsieur La Doulaise", cursive;
    font-size: 58px;
    line-height: 60px;
    color: var(--ink);
    border-bottom: 1px solid var(--rule);
  }

  /* Variant 5: solid bar */
  .tag-bar {
    position: absolute;
    left: 72px; top: 41px;
    width: 269px; height: 49px;
    background: var(--ink);
    border-radius: 0 8px 8px 0;
    color: var(--paper);
    font-family: "Exo 2", sans-serif;
    font-weight: 500;
    font-size: 30px;
    line-height: 49px;
    text-align: center;
    letter-spacing: 0.5px;
  }

  /* Variant 6: fine flourish script */
  .tag-fine {
    position: absolute;
    left: 0; right: 0; top: 18px;
    text-align: center;
    font-family: "Mrs Saint Delafield", cursive;
    font-size: 62px;
    line-height: 100px;
    color: var(--ink);
  }
</style>
</head>
<body>
<main class="sheet">

  <section class="label col-left row-1">
    <div class="tag-tab">For My<br>Friends</div>
    <div class="brand"><span class="brand-name">Nardi</span><span class="brand-product">ESPRESSO</span></div>
  </section>

  <section class="label col-right row-1">
    <div class="tag-flow">for my friends</div>
    <div class="brand"><span class="brand-name">Nardi</span><span class="brand-product">ESPRESSO</span></div>
  </section>

  <section class="label col-left row-2">
    <div class="tag-plate">For My Friends</div>
    <div class="brand"><span class="brand-name">Nardi</span><span class="brand-product">ESPRESSO</span></div>
  </section>

  <section class="label col-right row-2">
    <div class="tag-ruled">For My Friends</div>
    <div class="brand"><span class="brand-name">Nardi</span><span class="brand-product">ESPRESSO</span></div>
  </section>

  <section class="label col-left row-3">
    <div class="tag-bar">For My Friends</div>
    <div class="brand"><span class="brand-name">Nardi</span><span class="brand-product">ESPRESSO</span></div>
  </section>

  <section class="label col-right row-3">
    <div class="tag-fine">For My Friends</div>
    <div class="brand"><span class="brand-name">Nardi</span><span class="brand-product">ESPRESSO</span></div>
  </section>

</main>
</body>
</html>
```